Marla Quint Memoir

Book Cover Design
Title: Cedars and Salt
Subtitle: One Girl's Climb Through Kinship and Mercy
Author: Marla Quint
Book Description: Marla Quint’s memoir Cedars and Salt, follows five generations of one Alaskan family evolving with the rapidly changing landscape of the North. Few memoirs combine love of nature with love of family so eloquently, while at the same time acknowledging that each carries the potential for so much loss and pain. Through it all, this is the story of one woman’s quest to carve a place for herself in a rapidly changing land and claim her own unique power.
INSTRUCTIONS: Open to any interesting creative designs reflecting the above description. However, MUST include the attached photo on the cover in some way. Have also attached the .indd template for reference. Please leave bleed area plus 1/2 inch all around. On spine, leave two inches at bottom to allow for publisher's logo.

```html
<!DOCTYPE html>
<html lang="en">
<head>
<meta charset="utf-8">
<title>Cedars and Salt — Marla Quint</title>
<link rel="stylesheet" href="https://fonts.googleapis.com/css2?family=Open+Sans:wght@400;500&family=Open+Sans+Condensed:wght@300&family=Roboto+Condensed:wght@400&display=swap">
<style>
  :root {
    --page-bg: #e9e9e9;
    --ice-light: #c9dbe6;
    --ice-mid: #a9c3d3;
    --ice-deep: #8eabbf;
    --frost: #e6eff4;
    --leaf-dark: #2a1512;
    --leaf-warm: #6a3a22;
    --title-white: #f2f2f2;
    --ink: #141414;
  }
  * { box-sizing: border-box; margin: 0; padding: 0; }
  html, body {
    width: 1200px;
    height: 800px;
    overflow: hidden;
    background: var(--page-bg);
  }
  .canvas {
    position: relative;
    width: 1200px;
    height: 800px;
  }
  .book-cover {
    position: absolute;
    left: 366px;
    top: 42px;
    width: 468px;
    height: 716px;
    overflow: hidden;
  }
  .cover-photo {
    position: absolute;
    inset: 0;
    background:
      radial-gradient(ellipse 28% 22% at 52% 60%, var(--leaf-dark) 0%, var(--leaf-warm) 45%, rgba(230,239,244,0.0) 100%),
      radial-gradient(ellipse 48% 38% at 55% 62%, var(--frost) 0%, rgba(230,239,244,0) 80%),
      linear-gradient(160deg, var(--ice-light) 0%, var(--ice-mid) 55%, var(--ice-deep) 100%);
  }
  .title {
    position: absolute;
    left: 0;
    width: 100%;
    text-align: center;
    color: var(--title-white);
    font-family: "Open Sans", sans-serif;
    font-weight: 400;
    line-height: 1;
    text-shadow: 0 1px 2px rgba(60, 80, 95, 0.35);
  }
  .title-line-1 { top: 44px; font-size: 100px; letter-spacing: -1px; }
  .title-joiner { top: 146px; font-size: 33px; }
  .title-line-2 { top: 176px; font-size: 136px; letter-spacing: -2px; }
  .subtitle {
    position: absolute;
    left: 0;
    top: 578px;
    width: 100%;
    text-align: center;
    color: var(--ink);
    font-family: "Roboto Condensed", sans-serif;
    font-size: 18px;
    line-height: 24px;
    letter-spacing: 0.14em;
    text-transform: uppercase;
  }
  .author {
    position: absolute;
    left: 0;
    top: 649px;
    width: 100%;
    text-align: center;
    color: var(--ink);
    font-family: "Open Sans", sans-serif;
    font-weight: 400;
    font-size: 37px;
    line-height: 1;
    letter-spacing: 0.3em;
    padding-left: 0.3em;
    text-transform: uppercase;
  }
</style>
</head>
<body>
  <main class="canvas">
    <section class="book-cover">
      <div class="cover-photo" role="img" aria-label="Close-up photograph of a dark brown leaf frozen into pale blue river ice, frost crystals covering its lower half"></div>
      <h1 class="title-block">
        <span class="title title-line-1">CEDARS</span>
        <span class="title title-joiner">AND</span>
        <span class="title title-line-2">SALT</span>
      </h1>
      <p class="subtitle">One Girl's Climb Through<br>Kinship and Mercy</p>
      <p class="author">Marla Quint</p>
    </section>
  </main>
</body>
</html>
```